Business cards for Marrowfield Consulting with the following info for the front side:

Marrowfield Consulting
Executive Coaching and Human Capital Strategy
www.marrowfield.example

Idalia Renvoort
Principal
idalia@marrowfield.example
+1 555 274 9186

Black background, text using the colours of the logo - enclosed.

The back side of the business card should feature the logo in the middle, with "Executive Coaching and Human Capital Strategy" on top and "www.marrowfield.example" below.

```html
<!DOCTYPE html>
<html lang="en">
<head>
<meta charset="utf-8">
<title>Marrowfield Consulting — Business Cards</title>
<link rel="stylesheet" href="https://fonts.googleapis.com/css2?family=Lato:wght@400;700;900&display=swap">
<style>
  :root {
    --bg: #2b2b2d;
    --brand-blue: #30a2d9;
    --brand-yellow: #f7b917;
    --paper: #ffffff;
    --ink: #3a3a3a;
  }
  * { box-sizing: border-box; margin: 0; padding: 0; }
  html, body {
    width: 1200px; height: 900px; overflow: hidden;
    background: var(--bg);
    font-family: "Lato", sans-serif;
  }
  .canvas { position: relative; width: 1200px; height: 900px; }
  .card {
    position: absolute; left: 250px;
    width: 700px; height: 400px;
    border-radius: 22px; overflow: hidden;
  }

  /* Back side */
  .card--back { top: 30px; background: var(--brand-blue); color: var(--paper); }
  .card--back .brand {
    position: absolute; left: 120px; top: 118px;
    display: flex; align-items: center; gap: 18px;
  }
  .brand-dot {
    width: 84px; height: 84px; border-radius: 50%;
    border: 5px solid var(--paper);
    flex: none;
  }
  .card--back .brand-name {
    font-weight: 400; font-size: 54px; letter-spacing: 3px; line-height: 1;
    color: var(--paper);
  }
  .card--back .tagline {
    position: absolute; left: 222px; top: 190px;
    font-size: 17px; letter-spacing: 0.4px;
  }
  .card--back .web {
    position: absolute; left: 0; right: 0; top: 325px;
    text-align: center; font-size: 15px; letter-spacing: 5px;
  }
  .card--back .web .accent { color: var(--brand-yellow); }

  /* Front side */
  .card--front { top: 470px; background: var(--paper); }
  .card--front .wave { position: absolute; inset: 0; }
  .card--front .holder {
    position: absolute; right: 50px; top: 30px; text-align: right;
  }
  .holder-name {
    font-weight: 900; font-size: 34px; color: var(--brand-blue); line-height: 1.1;
  }
  .holder-role { font-size: 16px; color: var(--ink); margin-top: 2px; }
  .card--front .brand {
    position: absolute; left: 70px; top: 140px;
    display: flex; align-items: center; gap: 12px;
  }
  .card--front .brand-dot {
    width: 50px; height: 50px; border-color: var(--brand-blue); border-width: 4px;
  }
  .card--front .brand-name {
    font-weight: 400; font-size: 32px; letter-spacing: 2px; color: var(--brand-blue); line-height: 1;
  }
  .contact {
    position: absolute; right: 40px; top: 205px;
    text-align: right; color: var(--paper); font-size: 14px; line-height: 1.35;
  }
  .contact .company { font-weight: 700; font-size: 15px; }
  .contact .lines { margin-top: 10px; }
  .contact-row { display: flex; justify-content: flex-end; align-items: center; gap: 8px; }
  .contact-row svg { width: 14px; height: 14px; flex: none; }
</style>
</head>
<body>
<main class="canvas">

  <section class="card card--back" aria-label="Card back">
    <div class="brand">
      <span class="brand-dot"></span>
      <span class="brand-name">MARROWFIELD</span>
    </div>
    <p class="tagline">Executive Coaching and Human Capital Strategy</p>
    <p class="web">www.<span class="accent">marrowfield</span>.example</p>
  </section>

  <section class="card card--front" aria-label="Card front">
    <svg class="wave" viewBox="0 0 700 400" preserveAspectRatio="none" aria-hidden="true">
      <path d="M0,280 C240,300 360,260 450,175 C520,125 555,112 590,110 C550,120 515,140 470,185 C380,270 240,318 0,305 Z" fill="var(--brand-yellow)"/>
      <path d="M0,325 C240,325 380,285 470,215 C560,145 630,128 700,125 L700,400 L0,400 Z" fill="var(--brand-blue)"/>
    </svg>

    <div class="holder">
      <p class="holder-name">Idalia Renvoort</p>
      <p class="holder-role">Principal</p>
    </div>

    <div class="brand">
      <span class="brand-dot"></span>
      <span class="brand-name">MARROWFIELD</span>
    </div>

    <div class="contact">
      <p class="company">Marrowfield Consulting</p>
      <p>Executive Coaching and Human<br>Capital Strategy</p>
      <div class="lines">
        <p class="contact-row">+1 555 274 9186
          <svg viewBox="0 0 24 24" aria-hidden="true"><path fill="#fff" d="M6.6 10.8a15 15 0 0 0 6.6 6.6l2.2-2.2a1 1 0 0 1 1-.25 11.4 11.4 0 0 0 3.6.57 1 1 0 0 1 1 1V20a1 1 0 0 1-1 1A17 17 0 0 1 3 4a1 1 0 0 1 1-1h3.5a1 1 0 0 1 1 1c0 1.25.2 2.45.57 3.570a1 1 0 0 1-.25 1z"/></svg>
        </p>
        <p class="contact-row">idalia@marrowfield.example
          <svg viewBox="0 0 24 24" aria-hidden="true"><rect x="2" y="5" width="20" height="14" rx="1" fill="#fff"/><path d="M2 6l10 7 10-7" fill="none" stroke="var(--brand-blue)" stroke-width="1.6"/></svg>
        </p>
        <p class="contact-row">www.marrowfield.example
          <svg viewBox="0 0 24 24" aria-hidden="true"><g fill="none" stroke="#fff" stroke-width="1.8"><circle cx="12" cy="12" r="9"/><ellipse cx="12" cy="12" rx="4" ry="9"/><path d="M3 12h18M5 7h14M5 17h14"/></g></svg>
        </p>
      </div>
    </div>
  </section>

</main>
</body>
</html>
```